Psychiatrist/ Psychotherapist needs a letterhead design

I am a Psychiatrist working in private practice. I work as a psychotherapist and treat patients with depression, anxiety, post traumatic stress and relationship problems. I need a letterhead which is elegant and professional. I would like to see designs using colours such as blues and greys.
I would like the information on the letterhead split between the top and bottom of the page to give it a look of balance.
I want it to look elegant, feminine and upmarket. I don't want it to look too corporate but to show some flair and to be a bit artistic.

Target Market(s)

Other doctors, specialists and agencies who have referred patients to me.

Industry/Entity Type

Work

Font styles to use
Script

Requirements
Must have
• My name and my profession psychiatrist need to be highlighted and prominent. It needs to be professional looking and elegant without being old fashioned or too conservative.
Nice to have
• Balance between the top and bottom of the page.
Should not have
• I don't want fonts which are old and too traditional.

```html
<!DOCTYPE html>
<html lang="en">
<head>
<meta charset="utf-8">
<title>Dr. Clara Whitmore – Letterhead</title>
<link rel="stylesheet" href="https://fonts.googleapis.com/css2?family=Open+Sans:wght@400;600;700&display=swap">
<style>
  :root {
    --backdrop: #d9d9d9;
    --paper: #ffffff;
    --charcoal: #424245;
    --accent-blue: #1ba3dc;
    --ink: #4a4a4a;
    --ink-strong: #2e2e2e;
  }
  * { margin: 0; padding: 0; box-sizing: border-box; }
  html, body {
    width: 1006px;
    height: 1200px;
    overflow: hidden;
    background: var(--backdrop);
    font-family: "Open Sans", Arial, sans-serif;
  }
  .letterhead {
    position: absolute;
    left: 100px;
    top: 30px;
    width: 806px;
    height: 1140px;
    background: var(--paper);
    box-shadow: 0 4px 14px rgba(0, 0, 0, 0.18);
  }
  .name-block {
    position: absolute;
    left: 25px;
    top: 0;
    width: 220px;
    height: 141px;
    background: var(--charcoal);
    padding: 20px 0 0 14px;
    color: #fff;
    white-space: nowrap;
    overflow: hidden;
  }
  .name-first {
    font-size: 35px;
    font-weight: 700;
    line-height: 1;
    letter-spacing: -0.5px;
  }
  .name-last {
    font-size: 40px;
    font-weight: 700;
    line-height: 1.05;
    letter-spacing: -1px;
    margin-top: 3px;
  }
  .profession {
    font-size: 15.5px;
    font-weight: 700;
    color: var(--accent-blue);
    margin-top: 6px;
    letter-spacing: -0.2px;
  }
  .contact {
    position: absolute;
    right: 24px;
    top: 26px;
    text-align: right;
    font-size: 12.5px;
    line-height: 18px;
    color: var(--ink);
    white-space: nowrap;
  }
  .contact strong {
    font-weight: 700;
    color: var(--ink-strong);
  }
  .header-rule {
    position: absolute;
    left: 25px;
    top: 142px;
    width: 757px;
    height: 3px;
    background: var(--accent-blue);
  }
</style>
</head>
<body>
  <div class="letterhead">
    <div class="name-block">
      <div class="name-first">Dr. Clara</div>
      <div class="name-last">Whitmore</div>
      <div class="profession">Psychotherapist (B. Med)</div>
    </div>
    <div class="contact">
      <div>FRANZCP Psychiatrist 12</div>
      <div>Linden Avenue, Norwood, SA 5067</div>
      <div><strong>Tel:</strong> (08) 5550 1234</div>
      <div><strong>Fax:</strong> (08) 5550 1235</div>
      <div><strong>Mob:</strong> 0400555012</div>
      <div><strong>Email:</strong> cwhitmore@example.net</div>
    </div>
    <div class="header-rule"></div>
  </div>
</body>
</html>
```